Velmora Dried fruits

I am launching a dried fruit company in Nigeria (Velmora Dried fruit, or Velmora for Short), and looking for a packaging  design that reflects what my product is going to be about- quality, goodness, health, and lifestyle. It is a premium product and the packaging should reflect it. I also would like a logo created that instills the same values. Biblically, Velmora city was known as the land of "Milk and Honey" for me that incites images of health, abundance, wealth, and I'd love the logo and packaging to reflect this. Please note that due to the cost of printing. I'd like max of 2 colours to be used, bearing mind that the package must be translucent so that customers can see the product and will have writing on it.
I'd also like a logo to be created that imbibes the aforementioned  values. I am hoping "Velmora" becomes a recognized brand in the coming years, and I want the logo to be able to "stand alone" after I have built the brand

Upper Middle Class
It Company

```html
<!DOCTYPE html>
<html lang="en">
<head>
<meta charset="utf-8">
<title>Velmora Dried Fruits – Mango Pack</title>
<link href="https://fonts.googleapis.com/css2?family=Arimo:wght@400;700&display=swap" rel="stylesheet">
<style>
  :root {
    --page: #fbf4ea;
    --film: #efeee6;
    --film-edge: #dcdbd0;
    --crimp: #e3e2d8;
    --crimp-line: #d2d1c5;
    --gold: #e2a52a;
    --gold-deep: #c98a16;
    --gold-light: #f3c453;
    --brown: #6e5427;
    --ink: #5f4c2a;
  }
  * { box-sizing: border-box; margin: 0; padding: 0; }
  html, body {
    width: 1079px;
    height: 1200px;
    overflow: hidden;
  }
  body {
    background: var(--page);
    font-family: "Arimo", Arial, sans-serif;
    position: relative;
  }
  .pack {
    position: absolute;
    left: 190px;
    top: 200px;
    width: 700px;
    height: 800px;
    background: linear-gradient(180deg, #f3f2eb 0%, var(--film) 55%, #e9e8df 100%);
    border: 2px solid var(--film-edge);
  }
  .crimp {
    position: absolute;
    left: 0;
    right: 0;
    height: 46px;
    background: repeating-linear-gradient(180deg, var(--crimp) 0 7px, var(--crimp-line) 7px 9px);
  }
  .crimp--top { top: 0; }
  .crimp--bottom { bottom: 0; }

  .origin-mark {
    position: absolute;
    left: 38px;
    top: 140px;
    width: 150px;
    color: var(--gold);
  }
  .origin-mark__name {
    font-size: 26px;
    font-weight: 700;
    line-height: 1;
  }
  .origin-mark__tag {
    font-size: 8px;
    color: var(--brown);
    letter-spacing: 0.5px;
    margin-top: 4px;
    text-transform: uppercase;
  }

  .brand {
    position: absolute;
    left: 0;
    right: 0;
    top: 236px;
    text-align: center;
    color: var(--gold);
    font-weight: 700;
  }
  .brand__name {
    font-size: 104px;
    line-height: 1;
    letter-spacing: 1px;
  }
  .brand__sub {
    font-size: 28px;
    line-height: 1;
    letter-spacing: 4px;
    text-transform: uppercase;
    margin-top: 6px;
  }

  .flavour {
    position: absolute;
    left: 0;
    right: 0;
    top: 386px;
    text-align: center;
    font-size: 38px;
    font-weight: 700;
    color: var(--gold-deep);
    letter-spacing: 1px;
  }

  .claims {
    position: absolute;
    left: 0;
    right: 0;
    top: 452px;
    text-align: center;
    list-style: none;
    font-size: 21px;
    line-height: 28px;
    color: var(--ink);
    letter-spacing: 1px;
  }

  .net-weight {
    position: absolute;
    right: 172px;
    top: 592px;
    font-size: 20px;
    color: var(--ink);
    display: flex;
    align-items: center;
    gap: 3px;
  }
  .net-weight__estimate {
    font-size: 28px;
    font-weight: 700;
    color: var(--gold-deep);
    line-height: 1;
  }

  .nutrition {
    position: absolute;
    left: 146px;
    top: 622px;
    display: flex;
    gap: 4px;
  }
  .nutrition__item {
    width: 61px;
    height: 66px;
    background: var(--gold);
    border: 2px solid var(--gold-deep);
    border-radius: 12px 12px 3px 3px;
    text-align: center;
    color: var(--brown);
    display: flex;
    flex-direction: column;
    align-items: center;
    padding-top: 8px;
  }
  .nutrition__label {
    font-size: 8px;
    font-weight: 700;
    letter-spacing: 0.3px;
    text-transform: uppercase;
  }
  .nutrition__value {
    margin-top: 8px;
    width: 50px;
    background: var(--gold-light);
    border-radius: 3px;
    font-size: 17px;
    line-height: 26px;
  }
</style>
</head>
<body>
  <section class="pack" aria-label="Velmora Dried Fruits mango pack, front">
    <div class="crimp crimp--top"></div>

    <div class="origin-mark">
      <div class="origin-mark__name">Homegrown</div>
      <div class="origin-mark__tag">Good Food, Great Land</div>
    </div>

    <div class="brand">
      <div class="brand__name">Velmora</div>
      <div class="brand__sub">Dried Fruits</div>
    </div>

    <h1 class="flavour">MANGO</h1>

    <ul class="claims">
      <li>Delicious and Healthy</li>
      <li>Naturally Sweet</li>
      <li>No added Sugar</li>
      <li>Source of Fibre</li>
    </ul>

    <div class="net-weight">100g <span class="net-weight__estimate">℮</span></div>

    <div class="nutrition">
      <div class="nutrition__item"><span class="nutrition__label">Calories</span><span class="nutrition__value">314</span></div>
      <div class="nutrition__item"><span class="nutrition__label">Sugars</span><span class="nutrition__value">75g</span></div>
      <div class="nutrition__item"><span class="nutrition__label">Fibre</span><span class="nutrition__value">5g</span></div>
      <div class="nutrition__item"><span class="nutrition__label">Protein</span><span class="nutrition__value">1.5g</span></div>
      <div class="nutrition__item"><span class="nutrition__label">Fat</span><span class="nutrition__value">trace</span></div>
      <div class="nutrition__item"><span class="nutrition__label">Sodium</span><span class="nutrition__value">trace</span></div>
    </div>

    <div class="crimp crimp--bottom"></div>
  </section>
</body>
</html>
```